Business school needs a web design

Who We are:
KRVT is a small business school that offers programs in Project Management. The school is based in West Africa and welcomes students from the whole area. Our aim is to become one of the reference business schools in Africa.

Project Brief:
The site will include all informations relevant for different types of visitors that we have: actual and future students, companies, mass media, future employees, ect. It will present information about subscription, list of programs, presentation of the school and its team,etc.

What We want:
This competition is for Design only no coding! We need design for two pages.
We did some wireframing for the home page and the list of programs page. We made them just to show how we imagine the website would look like. But we encourage creative designs, so you don't have to stick to the wireframe models.

Sites We like:
http://www.ravenmoorcollege.example/
http://www.belvantis.example/fr/etudes.html
http://www.qtl.example/mba/Pages/default.aspx

Color schemes
The logo of the school is red and black. So the color scheme of the website should match that. For the rest, it is opened to your imagination.
Updates

The payment for the project is now garanteed. Good luck to you all !

Target Market(s)

The target market is diversified because we have students of different ages, also company representatives or employees that might visit the website for recruitment purposes. But the majority of our audience should be aged between 20 - 30 years.

Industry/Entity Type

Small Business

Requirements
Must have
• The design must include two pages: a home page and another interior page : might be the list of programs or any other page relevant to the domain. The Home page must include a slide show at the beginning.
The background page must be white.
Nice to have
• The use of flat design for this project is preferred.
The use of Pelican scaffold as a base for the design is an asset.

```html
<!DOCTYPE html>
<html lang="fr">
<head>
<meta charset="utf-8">
<title>KRVT — Programmes et Formation</title>
<link rel="stylesheet" href="https://fonts.googleapis.com/css2?family=Open+Sans:wght@400;600;700&display=swap">
<style>
:root{
  --red:#c4050c;
  --red-dark:#a30409;
  --wine:#7d2a2c;
  --wine-dark:#5e2a2c;
  --ink:#222;
  --text:#555;
  --grey-bg:#e8e8e8;
  --line:#bcbcbc;
  --footer:#2b2b2b;
  --white:#fff;
}
*{box-sizing:border-box;margin:0;padding:0}
html,body{width:1200px;height:2413px;overflow:hidden;background:var(--white);font-family:"Open Sans",Arial,sans-serif;color:var(--text)}
.page{position:relative;width:1200px;height:2413px}
.abs{position:absolute}

/* header */
.utility-bar{left:598px;top:0;width:567px;height:29px;background:var(--footer);border-radius:0 0 3px 3px;color:#eee;font-size:13px;display:flex;align-items:center;justify-content:center;gap:9px;letter-spacing:.3px}
.utility-bar .sep{color:#999}
.utility-bar .active{color:#f28a8a}
.brand{left:58px;top:60px;display:flex;align-items:center;gap:14px}
.brand-mark{width:40px;height:40px;background:var(--red);border-radius:50%}
.brand-name{font-size:46px;font-weight:700;color:var(--ink);letter-spacing:2px}
.social{left:1015px;top:74px;display:flex;gap:5px}
.social span{width:30px;height:30px;border-radius:2px}
.search{left:927px;top:125px;width:173px;height:33px;border:1px solid #ccc;border-radius:3px;font-size:13px;color:#aaa;padding:7px 10px}
.search-btn{left:1103px;top:125px;width:57px;height:33px;background:var(--red);border-radius:3px}
.main-nav{left:0;top:196px;width:1200px;height:57px;background:var(--red);display:flex;align-items:center;padding-left:54px;gap:32px;color:var(--white);font-size:18px;letter-spacing:.6px}
.nav-pointer{left:122px;top:253px;width:0;height:0;border-left:14px solid transparent;border-right:14px solid transparent;border-top:13px solid var(--red);z-index:3}

/* slider */
.slider{left:0;top:253px;width:1200px;height:532px;background:linear-gradient(180deg,#e6dcc5 0%,#c9b48c 40%,#8e7658 75%,#6a5640 100%)}
.slider-arrow{top:470px}
.slide-caption{left:846px;top:553px;width:354px;height:232px;background:rgba(40,40,40,.85);color:var(--white);padding:22px 28px}
.slide-caption h3{font-weight:400;font-size:19px;letter-spacing:.5px;margin-bottom:10px}
.slide-caption p{font-size:12.5px;line-height:21px;text-align:justify;color:#ddd}

/* intro section */
.intro{left:0;top:785px;width:1200px;height:703px;background:var(--grey-bg)}
.breadcrumb{left:50px;top:807px;display:flex;height:25px;font-size:12px;color:var(--white)}
.breadcrumb span{background:var(--red);padding:4px 14px 0 12px;clip-path:polygon(0 0,calc(100% - 10px) 0,100% 50%,calc(100% - 10px) 100%,0 100%)}
.breadcrumb span+span{background:var(--red-dark);margin-left:-2px;padding-left:20px;clip-path:polygon(0 0,calc(100% - 10px) 0,100% 50%,calc(100% - 10px) 100%,0 100%,10px 50%)}
.section-title{display:flex;align-items:center;gap:10px;font-size:27px;letter-spacing:2px;color:var(--ink);font-weight:400}
.section-title em{font-style:normal;color:var(--red)}
.section-title .rule{flex:1;height:5px;border-top:1px solid var(--line);border-bottom:1px solid var(--line)}
.video{left:60px;top:901px;width:532px;height:323px;background:linear-gradient(180deg,#e9e3cf 0%,#b3a27c 45%,#5e5342 100%)}
.video-bar{position:absolute;left:0;bottom:0;width:100%;height:26px;background:#1c1c1c}
.video-bar i{position:absolute;left:0;top:0;width:40px;height:4px;background:var(--red)}
.video-play{position:absolute;left:235px;top:126px;width:62px;height:44px;background:rgba(20,20,20,.85);border-radius:10px}
.video-play:after{content:"";position:absolute;left:25px;top:13px;border-left:16px solid #fff;border-top:9px solid transparent;border-bottom:9px solid transparent}
.thumb{top:1247px;height:117px}
.thumb-caption{top:1374px;font-size:12.5px;color:var(--red)}
.pager{left:539px;top:1407px;display:flex;gap:2px}
.pager span{width:24px;height:23px;background:#aaa;display:flex;align-items:center;justify-content:center}
.intro-text{left:616px;top:896px;width:520px;font-size:13.5px;line-height:22.5px;text-align:justify}
.intro-text p+p{margin-top:22px}
.btn{display:inline-flex;align-items:center;gap:5px;background:var(--red);color:var(--white);font-size:11.5px;letter-spacing:.5px;border-radius:2px}
.btn-intro{left:616px;top:1092px;width:132px;height:31px;justify-content:center}
.news{left:618px;top:1158px;width:514px;height:275px;background:var(--white);border:1px solid #ccc;border-radius:4px;padding:16px 0 0}
.news h4{font-weight:400;font-size:17px;color:var(--red);margin:0 0 8px 20px}
.news-item{display:flex;height:71px;padding:4px 16px;gap:10px}
.news-item:nth-child(odd){background:#fbe3e3}
.news-item .pic{width:113px;height:62px;background:linear-gradient(180deg,#7d7a86,#3b3e52)}
.news-item b{display:flex;justify-content:space-between;color:var(--red);font-size:14px}
.news-item b span{color:#333;font-weight:400}
.news-item p{font-size:13.5px;line-height:21px;color:var(--red-dark)}
.double-rule{left:58px;top:1449px;width:1092px;height:6px;border-top:1px solid var(--line);border-bottom:1px solid var(--line)}

/* programmes */
.programmes{left:0;top:1488px;width:1200px;height:648px;background:linear-gradient(135deg,#cfcfcf 0%,#a9a9a9 40%,#bdbdbd 70%,#8f8f8f 100%)}
.prog-card{top:1584px;width:303px;height:480px;background:var(--wine);color:var(--white);text-align:center}
.prog-card.alt{background:var(--wine-dark)}
.prog-card svg{position:absolute;left:48px;top:34px}
.prog-card h3{position:absolute;left:0;top:250px;width:100%;font-weight:400;font-size:22px;line-height:27px;letter-spacing:.8px}
.prog-card .dash{position:absolute;left:33px;width:237px;border-top:1px dashed #e9bdbd}
.prog-card p{position:absolute;left:34px;width:235px;font-size:12.5px;line-height:17.5px;text-align:justify;text-align-last:center}
.prog-card .btn{position:absolute;left:88px;top:411px;width:128px;height:28px;justify-content:center}
.prog-arrows{left:125px;top:2087px;display:flex;gap:4px}

/* footer */
.footer{left:0;top:2136px;width:1200px;height:238px;background:var(--footer);color:var(--white)}
.footer-title{left:52px;top:2152px;width:1096px;font-size:27px;letter-spacing:2px;color:var(--white)}
.footer-title .rule{border-color:#555}
.link-col{top:2210px;font-size:13.5px;letter-spacing:.5px}
.link-col h5{font-size:14px;font-weight:700;margin-bottom:10px}
.link-col li{list-style:none;font-size:12px;font-weight:700;height:26px;padding-left:14px;position:relative}
.link-col li:before{content:"";position:absolute;left:2px;top:6px;width:5px;height:5px;border-radius:50%;background:var(--white)}
.footer-bar{left:0;top:2374px;width:1200px;height:39px;background:var(--red);color:var(--white);font-size:12.5px;letter-spacing:.6px}
.footer-bar .legal{position:absolute;left:79px;top:11px}
.footer-bar .copy{position:absolute;right:110px;top:11px}
</style>
</head>
<body>
<div class="page">

  <header>
    <nav class="abs utility-bar">
      <span>Repertoire du personel</span><span class="sep">|</span>
      <span class="active">Blogue</span><span class="sep">|</span>
      <span>Solle de presse</span><span class="sep">|</span>
      <span>Nous joindre</span><span class="sep">|</span>
      <span>Francois</span>
    </nav>
    <div class="abs brand"><span class="brand-mark"></span><span class="brand-name">KRVT</span></div>
    <div class="abs social" aria-label="Réseaux sociaux">
      <span style="background:#3b5998"></span><span style="background:#2aa9e0"></span><span style="background:#0e76a8"></span><span style="background:#e34b2a"></span>
    </div>
    <div class="abs search">Search...</div>
    <div class="abs search-btn">
      <svg width="57" height="33" viewBox="0 0 57 33"><circle cx="26" cy="14" r="6" fill="none" stroke="#fff" stroke-width="3"/><line x1="30" y1="18" x2="36" y2="24" stroke="#fff" stroke-width="4" stroke-linecap="round"/></svg>
    </div>
    <nav class="abs main-nav">
      <span>A propos de l'KRVT</span><span>Programmes et Formations</span><span>Etudians</span><span>Nouvelles et Evenements</span><span>Enterprises</span>
    </nav>
    <div class="abs nav-pointer"></div>
  </header>

  <section class="abs slider" role="img" aria-label="Photo d'un amphithéâtre rempli d'étudiants face à une table de conférence"></section>
  <svg class="abs slider-arrow" style="left:40px" width="24" height="36" viewBox="0 0 24 36"><path d="M20 2 L5 18 L20 34" fill="none" stroke="#c4050c" stroke-width="6"/></svg>
  <svg class="abs slider-arrow" style="left:1150px" width="24" height="36" viewBox="0 0 24 36"><path d="M4 2 L19 18 L4 34" fill="none" stroke="#c4050c" stroke-width="6"/></svg>
  <div class="abs slide-caption">
    <h3>Title goes here</h3>
    <p>Lorem ipsum dolor sit amet, consectetur adipiscing elit. Pellentesque bibendum, lectus sit amet porta sagittis, orci eros vehicula justo, ac mollis metus felis eget dui. Nullam convallis magna dolor, non rhoncus leo faucibus vitae.</p>
  </div>

  <section class="abs intro"></section>
  <div class="abs breadcrumb"><span>Accueil</span><span>Programmes et Formation</span></div>
  <h2 class="abs section-title" style="left:52px;top:846px;width:1097px"><span><em>PROGRAMMES</em> ET FORMATION</span><span class="rule"></span></h2>

  <div class="abs video" role="img" aria-label="Vidéo d'un professeur donnant un cours dans une salle de classe">
    <span class="video-play"></span>
    <div class="video-bar"><i></i></div>
  </div>
  <div class="abs thumb" style="left:60px;width:168px;background:linear-gradient(180deg,#f2f2f2,#9a9a9a)" role="img" aria-label="Photo de gens d'affaires debout"></div>
  <div class="abs thumb" style="left:241px;width:172px;background:linear-gradient(180deg,#e8dfc6,#8b7754)" role="img" aria-label="Photo d'une salle de cours"></div>
  <div class="abs thumb" style="left:421px;width:171px;background:linear-gradient(180deg,#8a5a3a,#c8b9a4)" role="img" aria-label="Photo d'un étudiant devant une bibliothèque"></div>
  <span class="abs thumb-caption" style="left:60px">Lorem Ipsum Title</span>
  <span class="abs thumb-caption" style="left:241px">Lorem Ipsum Title</span>
  <span class="abs thumb-caption" style="left:421px">Lorem Ipsum Title</span>
  <div class="abs pager">
    <span><svg width="10" height="14"><path d="M8 1 L2 7 L8 13" fill="none" stroke="#fff" stroke-width="2"/></svg></span>
    <span style="background:#777"><svg width="10" height="14"><path d="M2 1 L8 7 L2 13" fill="none" stroke="#fff" stroke-width="2"/></svg></span>
  </div>

  <div class="abs intro-text">
    <p>Lorem ipsum dolor sit amet, consectetur adipiscing elit. Pellentesque bibendum, lectus sit amet porta sagittis, orci eros vehicula justo, ac mollis metus felis eget dui. Nullam convallis magna dolor, non rhoncus leo faucibus vitae.</p>
    <p>Donec pretium lorem quis odio euismod aliquet. Integer nec orci odio. In ullamcorper, ipsum at cursus luctus, velit tellus elementum ipsum, et feugiat dolor felis id massa.</p>
  </div>
  <a class="abs btn btn-intro">READ MORE ➡</a>

  <aside class="abs news">
    <h4>News &amp; Events</h4>
    <div>
      <div class="news-item"><div class="pic" role="img" aria-label="Photo d'étudiants en salle informatique"></div><div><b>Lorem Ipsum Title goes here <span>01/10/14</span></b><p>Donec pretium lorem quis odio euismod aliquet. Integer nec orci odio. In ullamcorper,</p></div></div>
      <div class="news-item"><div class="pic" role="img" aria-label="Photo d'étudiants en salle informatique"></div><div><b>Lorem Ipsum Title goes here <span>01/10/14</span></b><p>Donec pretium lorem quis odio euismod aliquet. Integer nec orci odio. In ullamcorper,</p></div></div>
      <div class="news-item"><div class="pic" role="img" aria-label="Photo d'étudiants en salle informatique"></div><div><b>Lorem Ipsum Title goes here <span>01/10/14</span></b><p>Donec pretium lorem quis odio euismod aliquet. Integer nec orci odio. In ullamcorper,</p></div></div>
    </div>
  </aside>
  <div class="abs double-rule"></div>

  <section class="abs programmes" role="img" aria-label="Photo en noir et blanc d'étudiants en salle de classe"></section>
  <h2 class="abs section-title" style="left:54px;top:1527px;width:1095px"><span><em>PROGRAMMES</em> OFFERTS</span><span class="rule"></span></h2>

  <article class="abs prog-card" style="left:122px">
    <svg width="208" height="208" viewBox="0 0 208 208"><circle cx="104" cy="104" r="99" fill="none" stroke="#fff" stroke-width="6"/>
      <path d="M40 88 L104 62 L168 88 L104 114 Z" fill="#fff"/><path d="M66 100 V132 Q104 152 142 132 V100 L104 116 Z" fill="#fff"/><line x1="160" y1="92" x2="160" y2="130" stroke="#fff" stroke-width="3"/></svg>
    <h3>Executive MBA</h3>
    <span class="dash" style="top:287px"></span>
    <p style="top:310px">Lorem ipsum dolor sit amet, consectetur adipiscing elit. Pellentesque bibendum, lectus sit amet porta sagittis.</p>
    <a class="btn">READ MORE ➡</a>
    <span class="dash" style="top:460px"></span>
  </article>

  <article class="abs prog-card alt" style="left:447px">
    <svg width="208" height="208" viewBox="0 0 208 208"><circle cx="104" cy="104" r="99" fill="none" stroke="#fff" stroke-width="6"/>
      <rect x="84" y="60" width="36" height="100" fill="#fff"/><rect x="98" y="36" width="8" height="26" fill="#fff"/><rect x="70" y="100" width="16" height="60" fill="#fff"/><rect x="118" y="90" width="18" height="70" fill="#fff"/><rect x="66" y="158" width="74" height="6" fill="#fff"/></svg>
    <h3>Master of International Business</h3>
    <span class="dash" style="top:312px"></span>
    <p style="top:335px">Lorem ipsum dolor sit amet, consectetur adipiscing elit. Pellentesque.</p>
    <a class="btn">READ MORE ➡</a>
    <span class="dash" style="top:460px"></span>
  </article>

  <article class="abs prog-card" style="left:775px">
    <svg width="208" height="208" viewBox="0 0 208 208"><circle cx="104" cy="104" r="99" fill="none" stroke="#fff" stroke-width="6"/>
      <path d="M88 60 L120 60 L112 76 Q150 96 150 128 Q150 158 104 158 Q58 158 58 128 Q58 96 96 76 Z" fill="#fff"/><text x="104" y="140" text-anchor="middle" font-family="Open Sans,Arial,sans-serif" font-size="40" font-weight="700" fill="#7d2a2c">$</text></svg>
    <h3>Master of Finance</h3>
    <span class="dash" style="top:287px"></span>
    <p style="top:310px">Lorem ipsum dolor sit amet, consectetur adipiscing elit. Pellentesque bibendum, lectus sit amet porta sagittis.</p>
    <a class="btn">READ MORE ➡</a>
    <span class="dash" style="top:460px"></span>
  </article>

  <div class="abs prog-arrows">
    <svg width="26" height="26" viewBox="0 0 26 26"><path d="M24 1 L2 13 L24 25 Z" fill="#888"/></svg>
    <svg width="26" height="26" viewBox="0 0 26 26"><path d="M2 1 L24 13 L2 25 Z" fill="#7d2a2c"/></svg>
  </div>

  <footer>
    <div class="abs footer"></div>
    <h2 class="abs section-title footer-title"><span>QUICKLINKS</span><span class="rule"></span></h2>
    <div class="abs link-col" style="left:93px"><h5>A propos de l'KRVT</h5><ul><li>Sublink 1</li><li>Sublink 2</li><li>Sublink 3</li><li>Sublink 4</li></ul></div>
    <div class="abs link-col" style="left:280px"><h5>Programmes et Formations</h5><ul><li>Sublink 1</li><li>Sublink 2</li><li>Sublink 3</li><li>Sublink 4</li></ul></div>
    <div class="abs link-col" style="left:534px"><h5>Etudians</h5><ul><li>Sublink 1</li><li>Sublink 2</li><li>Sublink 3</li><li>Sublink 4</li></ul></div>
    <div class="abs link-col" style="left:663px"><h5>Nouvelles et Evenements</h5><ul><li>Sublink 1</li><li>Sublink 2</li><li>Sublink 3</li><li>Sublink 4</li></ul></div>
    <div class="abs link-col" style="left:930px"><h5>Enterprises</h5><ul><li>Sublink 1</li><li>Sublink 2</li><li>Sublink 3</li></ul></div>
    <div class="abs footer-bar">
      <span class="legal">Sitemap &nbsp; / &nbsp; FAQ &nbsp; / &nbsp; Privacy Policy</span>
      <span class="copy">Copyright © 2014 KRVT</span>
    </div>
  </footer>

</div>
</body>
</html>
```